Bright Wave Labs

We need a professional letter head format for our company. Now we have a logo but need to desing a new logo also. I have uploaded our old logo. Use the color in the logo and design a new one.

Dear Designers , Need to mention "BWL" and please dont use our old LOGO. we need a new catchy one.

```html
<!DOCTYPE html>
<html lang="en">
<head>
<meta charset="utf-8">
<title>Bright Wave Labs Letterhead</title>
<link rel="stylesheet" href="https://fonts.googleapis.com/css2?family=Arimo:wght@700&family=Source+Sans+3:wght@400;600&display=swap">
<style>
  :root {
    --backdrop: #e6e6e6;
    --paper: #ffffff;
    --navy: #0d2240;
    --ink: #2b2b2b;
    --lime: #8dc63f;
    --sign-tone: #ececec;
  }
  html, body {
    margin: 0;
    width: 1200px;
    height: 1200px;
    overflow: hidden;
    background: var(--backdrop);
  }
  .letterhead {
    position: absolute;
    left: 190px;
    top: 20px;
    width: 820px;
    height: 1160px;
    background: var(--paper);
    font-family: "Source Sans 3", sans-serif;
    color: var(--ink);
  }
  .brand {
    position: absolute;
    left: 78px;
    top: 120px;
    display: flex;
    align-items: center;
    gap: 8px;
  }
  .brand-mark {
    width: 14px;
    height: 14px;
    background: var(--lime);
  }
  .brand-name {
    font-weight: 600;
    font-size: 17px;
    color: var(--navy);
    letter-spacing: 0.5px;
  }
  .greeting {
    position: absolute;
    left: 69px;
    top: 215px;
    margin: 0;
    font-family: "Arimo", sans-serif;
    font-weight: 700;
    font-size: 18px;
    color: var(--navy);
  }
  .body-copy {
    position: absolute;
    left: 69px;
    top: 262px;
    width: 686px;
  }
  .body-copy p {
    margin: 0 0 21px;
    font-size: 16.5px;
    line-height: 21.4px;
    text-align: justify;
  }
  .sign-off {
    position: absolute;
    left: 69px;
    top: 745px;
    width: 160px;
  }
  .signature {
    width: 140px;
    height: 52px;
    background: var(--sign-tone);
    border-radius: 4px;
  }
  .closing {
    margin: 2px 0 0 4px;
    font-weight: 600;
    font-size: 16px;
    color: var(--ink);
  }
  .footer-band {
    position: absolute;
    left: 0;
    bottom: 0;
    width: 820px;
    height: 30px;
    background: var(--navy);
    color: #ffffff;
    font-size: 12.5px;
  }
  .contact-list {
    position: absolute;
    left: 62px;
    top: 0;
    height: 30px;
    display: flex;
    align-items: center;
    gap: 8px;
    white-space: nowrap;
  }
  .contact-item {
    display: flex;
    align-items: center;
    gap: 3px;
  }
  .contact-item svg { width: 10px; height: 10px; }
  .web-tab {
    position: absolute;
    left: 582px;
    top: 0;
    width: 200px;
    height: 30px;
  }
  .web-tab svg { position: absolute; left: 0; top: 0; }
  .web-tab span {
    position: absolute;
    left: 16px;
    top: 0;
    line-height: 30px;
    font-size: 13.5px;
    letter-spacing: 0.8px;
    color: #ffffff;
  }
</style>
</head>
<body>
  <main class="letterhead">
    <header class="brand">
      <span class="brand-mark"></span>
      <span class="brand-name">BRIGHT WAVE LABS</span>
    </header>

    <h1 class="greeting">Dear Mr. John,</h1>

    <section class="body-copy">
      <p>Lorem Ipsum is simply dummy text of the printing and typesetting industry. Lorem Ipsum has been the industry's standard dummy text ever since the 1500s, when an unknown printer took a galley of type and scrambled it to make a type specimen book. It has survived not only five centuries, but also the leap into electronic typesetting, remaining essentially unchanged.</p>
      <p>The standard chunk of Lorem Ipsum used since the 1500s is reproduced below for those interested. Sections 1.10.32 and 1.10.33 from "de Finibus Bonorum et Malorum" by Cicero are also reproduced in their exact original form, accompanied by English versions from the 1914 translation by H. Rackham</p>
      <p>Lorem Ipsum is simply dummy text of the printing and typesetting industry. Lorem Ipsum has been the industry's standard dummy text ever since the 1500s, when an unknown printer took a galley of type and scrambled it to make a type specimen book. It has survived not only five centuries, but also the leap into electronic typesetting, remaining essentially unchanged. It was popularised in the</p>
      <p>The standard chunk of Lorem Ipsum used since the 1500s is reproduced below for those interested. Sections 1.10.32 and 1.10.33 from "de Finibus Bonorum et Malorum" by Cicero are also reproduced in their exact original form, accompanied by English versions from the 1914 translation by H. Rackham</p>
    </section>

    <div class="sign-off">
      <div class="signature" role="img" aria-label="Handwritten signature"></div>
      <p class="closing">Valued customers,</p>
    </div>

    <footer class="footer-band">
      <div class="contact-list">
        <span class="contact-item">
          <svg viewBox="0 0 10 10"><path d="M2 1 L4 1 L4.6 3 L3.4 4 Q4.5 6 6 6.6 L7 5.4 L9 6 L9 8 Q5 9 2 5 Q1 3 2 1 Z" fill="#8dc63f"/></svg>
          1-555-010-4821
        </span>
        <span class="contact-item">
          <svg viewBox="0 0 10 10"><rect x="0.5" y="2" width="9" height="6" fill="none" stroke="#8dc63f" stroke-width="1.2"/><path d="M0.5 2 L5 5.5 L9.5 2" fill="none" stroke="#8dc63f" stroke-width="1.2"/></svg>
          info@brightwavelabs.com
        </span>
        <span class="contact-item">
          <svg viewBox="0 0 10 10"><path d="M5 9.5 Q1.5 5.5 1.5 3.8 A3.5 3.5 0 0 1 8.5 3.8 Q8.5 5.5 5 9.5 Z" fill="none" stroke="#8dc63f" stroke-width="1.2"/><circle cx="5" cy="3.8" r="1.2" fill="#8dc63f"/></svg>
          Po. box 201, Street Name, City Name, - 00000
        </span>
      </div>
      <div class="web-tab">
        <svg width="200" height="30" viewBox="0 0 200 30">
          <polygon points="0,0 185,0 193,15 185,30 0,30 8,15" fill="#ffffff"/>
          <polygon points="2,0 183,0 191,15 183,30 2,30 10,15" fill="#8dc63f"/>
        </svg>
        <span>www.brightwavelabs.com</span>
      </div>
    </footer>
  </main>
</body>
</html>
```